Quarlwick Builders Business Cards

I want to use the logo and make an unique business card that shows the textured Logo with brick and builings. I want to be able to stand out when I pass out business cards.

```html
<!DOCTYPE html>
<html lang="en">
<head>
<meta charset="utf-8">
<title>Quarlwick Builders Business Cards</title>
<link href="https://fonts.googleapis.com/css2?family=Red+Hat+Display:wght@400;500;800&display=swap" rel="stylesheet">
<style>
  :root{
    --backdrop:#e6e5e6;
    --card-white:#ffffff;
    --card-black:#000000;
    --accent:#e8461f;
    --ink:#1a1a1a;
  }
  *{margin:0;padding:0;box-sizing:border-box}
  html,body{width:1200px;height:1108px;overflow:hidden}
  body{background:var(--backdrop);font-family:"Red Hat Display",sans-serif;position:relative}
  .card{position:absolute;left:214px;width:776px;height:472px}
  .card-front{top:50px;background:var(--card-white)}
  .card-back{top:574px;background:var(--card-black)}

  .brand-mark{position:absolute;display:flex;flex-direction:column;align-items:center;justify-content:center;
    color:var(--accent);font-weight:800;text-transform:uppercase;line-height:1;text-align:center}
  .card-front .brand-mark{left:168px;top:168px;width:222px;height:170px;font-size:34px;gap:4px}
  .card-back .brand-mark{left:218px;top:110px;width:340px;height:252px;font-size:54px;gap:8px}

  .divider{position:absolute;left:403px;top:154px;width:2px;height:208px;background:var(--accent)}
  .contact{position:absolute;left:430px;top:148px;color:var(--ink)}
  .contact-name{font-size:31px;font-weight:800;color:var(--accent);line-height:1.1}
  .contact-title{font-size:18px;font-weight:500;margin-top:2px}
  .contact-address{font-size:18px;line-height:22px;margin-top:18px}
  .contact-list{list-style:none;margin-top:16px}
  .contact-list li{display:flex;align-items:center;gap:10px;font-size:18px;height:28px}
  .contact-list svg{width:18px;height:18px;fill:var(--accent);flex:none}
</style>
</head>
<body>
  <section class="card card-front">
    <div class="brand-mark"><span>Quarlwick</span><span>Builders</span></div>
    <div class="divider"></div>
    <div class="contact">
      <div class="contact-name">Dana Whitfield</div>
      <div class="contact-title">Managing Director</div>
      <div class="contact-address">48 Harlow Lane,<br>Brookfield, USA</div>
      <ul class="contact-list">
        <li><svg viewBox="0 0 24 24"><path d="M3 8c0-3 4-4 9-4s9 1 9 4v2h-5V8H8v2H3zM6 11h12l2 9H4zM12 13a2.5 2.5 0 1 0 0 5a2.5 2.5 0 0 0 0-5z"/></svg>(08) 4630 2281</li>
        <li><svg viewBox="0 0 24 24"><path d="M2 5h20v2l-10 6L2 7zM2 9l10 6l10-6v10H2z"/></svg>info@quarlwickbuilders.com</li>
        <li><svg viewBox="0 0 24 24"><path d="M12 2a10 10 0 1 0 0 20a10 10 0 0 0 0-20zm-2 4c2 0 3 1 2 3s-3 1-3 3s2 2 1 4s-3 1-4-1c-1-3 1-5 0-6c1-2 3-3 4-3zm6 6c2 0 3 2 2 4s-3 1-3-1s-1-3 1-3z"/></svg>www.quarlwickbuilders.com</li>
      </ul>
    </div>
  </section>

  <section class="card card-back">
    <div class="brand-mark"><span>Quarlwick</span><span>Builders</span></div>
  </section>
</body>
</html>
```